Nimble Bench Gigs website

Our business is a freelance marketplace for IT and Digital contractors. It will provide a way for companies to take advantage of specialist talent for small periods of time and engage with them on a flexible basis. Logo should be something that shows Knowledge, Agility, Unlocking. Modern, simple, genius.We are looking for a site that conveys three things:- To have great technology you need great software, great hardware and great people. No one argues with that. To spend your dollars wisely and to focus on your core business, you have Cloud software and Cloud Hardware. Are any of your people in the cloud?- 5 specialists for the cost of one generalist- Cloud, agile and communication are converging to make the business case for remote specialists irresistible, we can get you the people you need to get your projects done, today.

Target Market(s)

Businesses, Tech professionals, Sales People, Recruiters

Industry/Entity Type

Information Technology

Logo Text

NimbleBenchGigs or NBG

Coding

Coded - Design and coding required

Number of Pages Required

5+ page

Font styles to use
Sans Serif

Colors

Designer to choose colors to be used in the design.

Requirements
Must have
• A beautiful landing page with a technical feel to it
• a nice slick graphic for the How it works...
• A look and feel that is consistent throughout
• Some moving text
Should not have
• ugly anything

```html
<!DOCTYPE html>
<html lang="en">
<head>
<meta charset="utf-8">
<title>Nimble Bench Gigs</title>
<link href="https://fonts.googleapis.com/css2?family=Montserrat:wght@700;800&family=Roboto:wght@400;500;700&family=Roboto+Condensed:wght@700&display=swap" rel="stylesheet">
<style>
:root{
  --blue:#0f6fc6;
  --blue-dark:#0a55a3;
  --orange:#ef5a35;
  --navy:#17294a;
  --teal:#2bb7c4;
  --yellow:#f5b400;
  --ink:#333333;
  --body:#666666;
  --white:#ffffff;
}
*{margin:0;padding:0;box-sizing:border-box}
html,body{width:1200px;height:2307px;overflow:hidden;background:var(--white)}
.page{position:relative;width:1200px;height:2307px;font-family:Roboto,Arial,sans-serif;color:var(--ink)}
.backdrop{position:absolute;left:0;top:0}
.abs{position:absolute}
.brand{left:145px;top:44px;display:flex;align-items:center;gap:10px}
.brand-dot{width:34px;height:34px;border-radius:50%;background:var(--orange)}
.brand-name{font-family:Montserrat,sans-serif;font-weight:800;font-size:24px;color:var(--white)}
.nav{top:55px;left:566px;display:flex;gap:23px;font-size:14px;color:var(--white);font-weight:500}
.cta{left:916px;top:47px;width:139px;height:33px;border-radius:17px;background:var(--orange);color:var(--white);font-size:13px;font-weight:700;display:flex;align-items:center;justify-content:center}
.hero-title{left:0;width:1200px;top:222px;text-align:center;font-family:Montserrat,sans-serif;font-weight:800;font-size:54px;color:var(--white);letter-spacing:-1px}
.hero-title span{color:var(--orange)}
.hero-sub{left:0;width:1200px;top:303px;text-align:center;font-size:22px;font-weight:500;color:var(--white)}
.hero-ask{left:390px;top:355px;width:420px;height:55px;background:var(--navy);color:var(--white);font-family:"Roboto Condensed",sans-serif;font-weight:700;font-size:37px;display:flex;align-items:center;justify-content:center}
.role{font-size:22px;font-weight:700;color:var(--white);text-align:center;width:180px}
.section-title{left:0;width:1200px;text-align:center;font-family:Montserrat,sans-serif;font-weight:800;color:var(--ink)}
.step h3{font-family:Montserrat,sans-serif;font-weight:700;font-size:21px;color:var(--ink);margin-bottom:12px;letter-spacing:.5px}
.step p{font-size:13px;line-height:21px;color:var(--body)}
.step .more{display:block;margin-top:12px;font-size:13px;font-weight:500}
.step-business{left:130px;width:284px;top:934px;text-align:right}
.step-business .more{color:var(--teal)}
.step-affiliate{left:786px;width:290px;top:872px}
.step-affiliate .more{color:var(--yellow)}
.step-specialists{left:471px;width:320px;top:1444px;text-align:center}
.step-specialists .more{color:var(--teal)}
.hub{left:500px;width:200px;top:1142px;text-align:center;font-family:Montserrat,sans-serif;font-weight:800;font-size:34px;color:var(--blue)}
.ghost{left:940px;top:1300px;width:100px;height:330px;font-family:Montserrat,sans-serif;font-weight:800;font-size:78px;color:#ececec;writing-mode:vertical-rl;transform:rotate(180deg);text-align:left}
.scene{left:40px;top:1424px;width:336px;height:179px;border-radius:40px;background:radial-gradient(ellipse at center,#f6a25a 0%,#3f7fcf 55%,#f4f4f4 80%)}
.stats-title{top:1730px;color:var(--white);font-size:42px}
.stat{width:196px;text-align:center;color:var(--white);top:1868px}
.stat b{display:block;font-family:Montserrat,sans-serif;font-weight:800;font-size:38px;margin-bottom:12px}
.stat span{display:block;font-size:19px;font-weight:500;line-height:26px}
.foot-brand{left:196px;width:240px;top:2125px;text-align:center}
.foot-dot{width:44px;height:44px;border-radius:50%;background:var(--orange);margin:0 auto 16px}
.foot-name{font-family:Montserrat,sans-serif;font-weight:800;font-size:21px;color:var(--blue)}
.socials{left:238px;top:2241px;display:flex;gap:4px}
.socials i{display:block;width:36px;height:36px;border-radius:50%}
.foot-nav{left:493px;top:2172px;font-size:20px;font-weight:500;color:var(--ink);word-spacing:2px}
.foot-nav em{font-style:normal;margin:0 14px}
.copy{left:493px;top:2217px;font-size:13px;color:var(--body)}
</style>
</head>
<body>
<div class="page">
<svg class="backdrop" width="1200" height="2307" viewBox="0 0 1200 2307">
  <defs>
    <linearGradient id="heroFill" x1="0" y1="0" x2="1" y2="0.3">
      <stop offset="0" stop-color="#0b0d12"/>
      <stop offset="0.45" stop-color="#2b3a48"/>
      <stop offset="0.75" stop-color="#4f86b3"/>
      <stop offset="1" stop-color="#2f78c0"/>
    </linearGradient>
    <linearGradient id="statsFill" x1="0" y1="0" x2="0" y2="1">
      <stop offset="0" stop-color="#f07d5e"/>
      <stop offset="1" stop-color="#e9522f"/>
    </linearGradient>
    <radialGradient id="statBall" cx="0.5" cy="0.3" r="0.7">
      <stop offset="0" stop-color="#1a8ae0"/>
      <stop offset="1" stop-color="#0a56a8"/>
    </radialGradient>
    <filter id="soft" x="-30%" y="-30%" width="160%" height="160%">
      <feDropShadow dx="0" dy="6" stdDeviation="8" flood-color="#000" flood-opacity="0.18"/>
    </filter>
  </defs>

  <!-- hero -->
  <path role="img" aria-label="Photo of a smiling young man in a denim shirt working on a laptop at a desk" d="M0 0H1200V540Q600 630 0 535Z" fill="url(#heroFill)"/>
  <path d="M0 535Q300 600 600 610Q900 600 1200 530" fill="none" stroke="var(--blue)" stroke-width="12"/>
  <path d="M0 541Q300 606 600 616Q900 606 1200 536V560H0Z" fill="#fff"/>

  <!-- role circles -->
  <g filter="url(#soft)">
    <circle cx="407" cy="600" r="91" fill="var(--blue)" stroke="#0b5db0" stroke-width="4"/>
    <circle cx="793" cy="600" r="91" fill="var(--blue)" stroke="#0b5db0" stroke-width="4"/>
    <circle cx="600" cy="600" r="112" fill="var(--orange)" stroke="#d9492a" stroke-width="6"/>
  </g>
  <g fill="none" stroke="#fff" stroke-width="2.5" stroke-linecap="round" stroke-linejoin="round">
    <circle cx="398" cy="565" r="13"/>
    <path d="M378 612v-16q0-12 20-12q18 0 20 12"/>
    <rect x="414" y="550" width="24" height="18" rx="3"/>
    <path d="M419 556h14M419 562h9"/>
    <circle cx="600" cy="551" r="11"/>
    <path d="M582 585q0-20 18-20q18 0 18 20z"/>
    <path d="M573 593l4 8 8 1-6 6 2 8-8-4-8 4 2-8-6-6 8-1z M600 593l4 8 8 1-6 6 2 8-8-4-8 4 2-8-6-6 8-1z M627 593l4 8 8 1-6 6 2 8-8-4-8 4 2-8-6-6 8-1z"/>
    <circle cx="793" cy="583" r="20"/>
    <circle cx="783" cy="582" r="4"/><circle cx="793" cy="580" r="4"/><circle cx="803" cy="582" r="4"/>
    <path d="M793 553v-12M789 545l4-4 4 4M793 613v-12M789 609l4 4 4-4M761 583h-10M755 579l-4 4 4 4M825 583h10M831 579l4 4-4 4"/>
  </g>

  <!-- diagram -->
  <g fill="#f4f4f4" filter="url(#soft)">
    <circle cx="600" cy="1011" r="142"/>
    <circle cx="466" cy="1254" r="142"/>
    <circle cx="734" cy="1254" r="142"/>
  </g>
  <g>
    <circle cx="600" cy="1021" r="112" fill="var(--teal)"/>
    <polygon points="421,1109 584,1132 502,966" fill="var(--teal)"/>
    <circle cx="466" cy="1254" r="112" fill="#e8431f"/>
    <polygon points="631,1368 465,1366 570,1213" fill="#e8431f"/>
    <circle cx="734" cy="1254" r="112" fill="var(--yellow)"/>
    <polygon points="748,1055 646,1185 831,1198" fill="var(--yellow)"/>
  </g>
  <g fill="#f1f1f1" stroke="#fff" stroke-width="6" filter="url(#soft)">
    <circle cx="600" cy="1021" r="94"/>
    <circle cx="466" cy="1254" r="94"/>
    <circle cx="734" cy="1254" r="94"/>
  </g>
  <g fill="none" stroke-width="2.5" stroke-linecap="round" stroke-linejoin="round">
    <g stroke="var(--blue)">
      <circle cx="600" cy="1003" r="22"/>
      <circle cx="600" cy="1003" r="9"/>
      <path d="M556 1030l22-10 22 12 22-12 22 10v20l-22 14-22-8-22 8-22-14z"/>
      <path d="M578 1044l14 10M590 1040l14 12M604 1040l10 10"/>
    </g>
    <g stroke="#e8431f">
      <circle cx="466" cy="1223" r="14" stroke-dasharray="3 3"/>
      <path d="M466 1214l3 6 6 1-4 4 1 6-6-3-6 3 1-6-4-4 6-1z"/>
      <circle cx="430" cy="1255" r="7"/><path d="M418 1288v-14q0-9 12-9q12 0 12 9v14z"/>
      <circle cx="466" cy="1258" r="8"/><path d="M452 1294v-16q0-10 14-10q14 0 14 10v16z"/>
      <circle cx="502" cy="1255" r="7"/><path d="M490 1288v-14q0-9 12-9q12 0 12 9v14z"/>
      <path d="M430 1236l2 4 4 1-3 3 1 4-4-2-4 2 1-4-3-3 4-1zM502 1236l2 4 4 1-3 3 1 4-4-2-4 2 1-4-3-3 4-1z"/>
    </g>
    <g stroke="var(--yellow)">
      <circle cx="734" cy="1228" r="22"/><circle cx="734" cy="1222" r="8"/><path d="M721 1242q13-12 26 0"/>
      <circle cx="708" cy="1277" r="22"/><circle cx="708" cy="1271" r="8"/><path d="M695 1291q13-12 26 0"/>
      <circle cx="760" cy="1277" r="22"/><circle cx="760" cy="1271" r="8"/><path d="M747 1291q13-12 26 0"/>
    </g>
  </g>
  <g fill="none" stroke-width="2">
    <path d="M373 1079v30h48" stroke="var(--teal)"/>
    <path d="M857 1023v32h-109" stroke="var(--yellow)"/>
    <path d="M631 1368v63" stroke="#e8431f"/>
  </g>
  <g fill="#bbb"><circle cx="373" cy="1079" r="3"/><circle cx="857" cy="1023" r="3"/><circle cx="631" cy="1431" r="3"/></g>

  <!-- stats band -->
  <path role="img" aria-label="Faded photo of a person with a laptop and technology line graphics" d="M0 1712Q600 1600 1200 1686V2017Q600 2170 0 2042Z" fill="url(#statsFill)"/>
  <path d="M0 1712Q600 1600 1200 1686" fill="none" stroke="var(--blue)" stroke-width="8" stroke-dasharray="0 0"/>
  <path d="M0 1712Q300 1660 600 1645" fill="none" stroke="var(--blue)" stroke-width="8"/>
  <path d="M600 2115Q900 2100 1200 2017" fill="none" stroke="var(--blue)" stroke-width="8"/>
  <g filter="url(#soft)" fill="url(#statBall)" stroke="#0c5fb5" stroke-width="4">
    <circle cx="244" cy="1918" r="98"/>
    <circle cx="479" cy="1918" r="98"/>
    <circle cx="714" cy="1918" r="98"/>
    <circle cx="948" cy="1918" r="98"/>
  </g>
  <g fill="var(--orange)" stroke="#fff" stroke-width="4">
    <circle cx="328" cy="1867" r="21"/>
    <circle cx="563" cy="1867" r="21"/>
    <circle cx="797" cy="1867" r="21"/>
    <circle cx="1032" cy="1867" r="21"/>
  </g>
  <g fill="none" stroke="#fff" stroke-width="2" stroke-linecap="round">
    <circle cx="328" cy="1861" r="5" fill="#fff"/><path d="M319 1876q9-10 18 0z" fill="#fff"/>
    <rect x="554" y="1859" width="18" height="12" rx="1"/><path d="M563 1871v4M558 1876h10"/>
    <circle cx="797" cy="1867" r="9"/><path d="M797 1862v5l3 3"/>
    <circle cx="1032" cy="1867" r="9"/><path d="M1032 1862v5h4"/>
  </g>
</svg>

<header>
  <div class="abs brand"><span class="brand-dot"></span><span class="brand-name">NIMBLE BENCH GIGS</span></div>
  <nav class="abs nav"><span>HOW IT WORKS</span><span>LOGIN</span><span>SIGN UP</span><span>COMPANY</span></nav>
  <div class="abs cta">START SIDE JOB</div>
</header>

<section class="hero">
  <h1 class="abs hero-title">NIMBLE BENCH <span>GIGS</span></h1>
  <p class="abs hero-sub">Sed ut perspiciatis unde omnisnatu</p>
  <p class="abs hero-ask">DO YOU WANT TO BE A</p>
  <div class="abs role" style="left:317px;top:630px">GIGGER</div>
  <div class="abs role" style="left:510px;top:640px">CUSTOMER</div>
  <div class="abs role" style="left:703px;top:630px">AFFILIATE</div>
</section>

<section class="how">
  <h2 class="abs section-title" style="top:786px;font-size:40px">HOW IT WORKS</h2>
  <div class="abs step step-business">
    <h3>BUSINESS</h3>
    <p>Sed ut perspiciatis unde omnis iste natus error<br>sit voluptatem accusantium doloremque<br>laudantium totam rem aperiam,</p>
    <span class="more">READ MORE</span>
  </div>
  <div class="abs step step-affiliate">
    <h3>AFFILIATE</h3>
    <p>Sed ut perspiciatis unde omnis iste natus error<br>sit voluptatem accusantium doloremque<br>laudantium totam rem aperiam,</p>
    <span class="more">READ MORE</span>
  </div>
  <div class="abs hub">NBG</div>
  <div class="abs step step-specialists">
    <h3>SPECIALISTS</h3>
    <p>Sed ut perspiciatis unde omnis iste natus error<br>sit voluptatem accusantium doloremque<br>laudantium totam rem aperiam,</p>
    <span class="more">READ MORE</span>
  </div>
  <div class="abs scene" role="img" aria-label="Illustration of freelancers working on laptops among books and plants"></div>
  <div class="abs ghost">HOW IT</div>
</section>

<section class="stats">
  <h2 class="abs section-title stats-title">OUR STATS</h2>
  <div class="abs stat" style="left:146px"><b>100%</b><span>REFERRAL<br>CLIENTS</span></div>
  <div class="abs stat" style="left:381px"><b>80%</b><span>FREELANCING<br>PLATFORMS</span></div>
  <div class="abs stat" style="left:616px"><b>60%</b><span>FULL TIME<br>FREELANCERS</span></div>
  <div class="abs stat" style="left:850px"><b>20%</b><span>PART TIME<br>FREELANCERS</span></div>
</section>

<footer>
  <div class="abs foot-brand"><div class="foot-dot"></div><div class="foot-name">NIMBLE BENCH GIGS</div></div>
  <div class="abs socials" aria-label="Social links">
    <i style="background:#1d3f8f"></i><i style="background:#1a9be0"></i><i style="background:#e2342c"></i><i style="background:#a98a5c"></i>
  </div>
  <nav class="abs foot-nav">HOW IT WORKS<em>/</em>LOGIN<em>/</em>SIGN UP<em>/</em>COMPANY</nav>
  <p class="abs copy">Copyrights © 2019, Nimble Bench Gigs.All Rights Reserved &nbsp;|&nbsp; Privacy policy</p>
</footer>
</div>
</body>
</html>
```